Garrick and Mott Personal Injury Billboard

We'd like a clean/modern billboard to build brand awareness for our law firm in the area of personal injury. Ideally, we like the word "Injured?" or something similar in large lettering.

I'm attaching images, logo and award badges which could be used. The billboards will be 14x48 ft and 10.6x36.

We are open to different color ideas, fonts, and artwork. Creative but not too busy with wording. Our web page is www.tgarrickfirm.example

Garrick & Mott Law Firm
(555) 318-4092

```html
<!DOCTYPE html>
<html lang="en">
<head>
<meta charset="utf-8">
<title>Garrick &amp; Mott Personal Injury Billboard</title>
<link rel="stylesheet" href="https://fonts.googleapis.com/css2?family=Cinzel:wght@500&family=Montserrat:wght@600;800&display=swap">
<style>
  :root {
    --navy: #0e1150;
    --paper: #ffffff;
    --sky: #1ba6ea;
    --stage: #eef1f4;
  }
  * { margin: 0; padding: 0; box-sizing: border-box; }
  html, body { width: 1200px; height: 1186px; overflow: hidden; background: var(--stage); }
  .billboard {
    position: absolute; left: 0; top: 418px;
    width: 1200px; height: 349px;
    background: var(--navy);
    overflow: hidden;
  }
  .headline-band {
    position: absolute; left: 216px; top: 42px;
    width: 768px; height: 186px;
    background: var(--paper);
  }
  .frame-lines { position: absolute; top: 47px; width: 22px; height: 196px; }
  .frame-lines.left { left: 190px; }
  .frame-lines.right { left: 986px; }
  .headline {
    position: absolute; left: 216px; top: 62px; width: 768px;
    text-align: center;
    font-family: "Cinzel", serif; font-weight: 500;
    font-size: 148px; line-height: 1; letter-spacing: 4px;
    color: var(--navy);
  }
  .award-badge { position: absolute; left: 1076px; top: 0; width: 88px; height: 140px; }
  .phone-box {
    position: absolute; left: 0; top: 266px; width: 484px; height: 59px;
    background: var(--paper);
    display: flex; align-items: center; justify-content: center;
    font-family: "Montserrat", sans-serif; font-weight: 800;
    font-size: 44px; color: var(--navy); letter-spacing: -0.5px;
    white-space: nowrap;
  }
  .firm-name {
    position: absolute; left: 496px; top: 254px; width: 176px;
    font-family: "Montserrat", sans-serif; font-weight: 600;
    color: var(--paper); text-align: center; line-height: 1;
    white-space: nowrap;
  }
  .firm-name .primary { display: block; font-size: 26px; letter-spacing: 1px; }
  .firm-name .primary + .primary { margin-top: 3px; }
  .firm-name .secondary { display: block; font-size: 11px; letter-spacing: 3px; margin-top: 7px; }
  .divider { position: absolute; left: 678px; top: 247px; width: 14px; height: 92px; }
  .web-bar {
    position: absolute; left: 716px; top: 266px; width: 484px; height: 59px;
    background: var(--sky);
    display: flex; align-items: center; padding-left: 14px;
    font-family: "Montserrat", sans-serif; font-weight: 800;
    font-size: 28px; color: var(--navy); letter-spacing: 0.5px;
    white-space: nowrap;
  }
</style>
</head>
<body>
  <section class="billboard">
    <div class="headline-band" aria-hidden="true"></div>
    <svg class="frame-lines left" viewBox="0 0 22 196" preserveAspectRatio="none" aria-hidden="true">
      <rect x="0" y="0" width="4" height="196" fill="var(--paper)"/>
      <rect x="16" y="0" width="6" height="196" fill="var(--paper)"/>
    </svg>
    <svg class="frame-lines right" viewBox="0 0 22 196" preserveAspectRatio="none" aria-hidden="true">
      <rect x="0" y="0" width="6" height="196" fill="var(--paper)"/>
      <rect x="18" y="0" width="4" height="196" fill="var(--paper)"/>
    </svg>
    <h1 class="headline">INJURED?</h1>

    <svg class="award-badge" viewBox="0 0 88 140" role="img" aria-label="Award badge">
      <polygon points="0,0 88,0 88,140 44,118 0,140" fill="var(--paper)"/>
      <rect x="10" y="16" width="68" height="86" fill="var(--sky)"/>
      <rect x="14" y="20" width="60" height="78" fill="var(--navy)"/>
    </svg>

    <div class="phone-box">(555) 318-4092</div>
    <div class="firm-name">
      <span class="primary">GARRICK</span>
      <span class="primary">&amp; MOTT</span>
      <span class="secondary">Law Firm</span>
    </div>
    <svg class="divider" viewBox="0 0 14 92" preserveAspectRatio="none" aria-hidden="true">
      <rect x="0" y="0" width="3" height="92" fill="var(--paper)"/>
      <rect x="10" y="0" width="3" height="92" fill="var(--paper)"/>
    </svg>
    <div class="web-bar">www.tgarrickfirm.example</div>
  </section>
</body>
</html>
```